Wedding logo

a simple design to be used on letterhead/menus for wedding
" Lorena & Victor"
palm branch or similar - tropical foliage

Industry/Entity Type

Wedding

Font styles to use
Decorative
Script

Colors
9bcb3c

Requirements
Must have
• names
• green foliage
Nice to have
• similar font to picture sent
Should not have
• too much color

```html
<!DOCTYPE html>
<html lang="en">
<head>
<meta charset="utf-8">
<title>Lorena &amp; Victor — Wedding Letterhead</title>
<link rel="stylesheet" href="https://fonts.googleapis.com/css2?family=Parisienne&family=Roboto:wght@400&family=Open+Sans:wght@700&display=swap">
<style>
  :root {
    --canvas: #ffffff;
    --paper: #fdfadf;
    --leaf-dark: #2f6b2a;
    --leaf-mid: #4e9a35;
    --leaf-light: #9bcb3c;
    --ink-green: #2d5a27;
    --ink-body: #4d5560;
    --ink-label: #000000;
    --shadow: #555555;
    --edge: #9a9a9a;
  }
  * { margin: 0; padding: 0; box-sizing: border-box; }
  html, body { width: 1199px; height: 1200px; overflow: hidden; background: var(--canvas); }
  .board { position: relative; width: 1199px; height: 1200px; }

  .sheet {
    position: absolute;
    width: 600px;
    height: 834px;
    background: var(--paper);
    border: 1px solid var(--edge);
    box-shadow: 12px 12px 0 var(--shadow);
    overflow: hidden;
  }
  .sheet--text { left: 48px; top: 43px; z-index: 1; }
  .sheet--blank { left: 548px; top: 271px; z-index: 2; }

  .foliage { position: absolute; display: block; }
  .foliage--top { left: 0; top: 0; width: 600px; height: 190px; }
  .foliage--corner { left: 0; bottom: 0; width: 300px; height: 275px; }

  .recipient {
    position: absolute; left: 36px; top: 142px;
    font-family: "Parisienne", cursive;
    color: var(--ink-green);
    font-size: 27px; line-height: 28px;
  }
  .contact {
    position: absolute; left: 371px; top: 162px;
    font-family: "Roboto", sans-serif;
    font-size: 10.5px; line-height: 17px;
    color: var(--ink-body);
    list-style: none;
  }
  .letter-body {
    position: absolute; left: 32px; top: 260px; width: 545px;
    font-family: "Roboto", sans-serif;
    font-size: 10.5px; line-height: 17px;
    color: var(--ink-body);
  }
  .letter-body p { margin-bottom: 17px; }

  .couple {
    position: absolute; left: 322px; top: 678px;
    font-family: "Parisienne", cursive;
    color: var(--ink-green);
    font-size: 47px; line-height: 50px;
  }
  .couple__second { display: block; padding-left: 70px; }

  .label {
    position: absolute;
    font-family: "Open Sans", sans-serif;
    font-weight: 700;
    font-size: 33px;
    color: var(--ink-label);
    white-space: nowrap;
  }
  .label--text { left: 706px; top: 133px; }
  .label--blank { left: 114px; top: 952px; }
</style>
</head>
<body>
<main class="board">

  <section class="sheet sheet--text">
    <svg class="foliage foliage--top" viewBox="0 0 600 190" role="img" aria-label="Border of tropical leaves with pink hibiscus, frangipani flowers and a butterfly">
      <defs>
        <linearGradient id="topLeavesA" x1="0" y1="0" x2="0" y2="1">
          <stop offset="0" stop-color="var(--leaf-mid)"/>
          <stop offset="1" stop-color="var(--leaf-dark)"/>
        </linearGradient>
      </defs>
      <path d="M0 0 H600 V110 C570 130 545 120 520 100 C495 125 470 140 440 120 C410 130 385 125 365 105 C340 135 315 150 285 140 C260 125 235 130 210 118 C190 95 160 92 140 82 C110 100 80 95 55 80 C35 95 15 90 0 85 Z" fill="url(#topLeavesA)"/>
    </svg>

    <p class="recipient">To<br>Noah Bennett</p>

    <ul class="contact">
      <li>Address: 27 Fernleaf Lane, Marlow Bay 40</li>
      <li>Web: www.palmgrovepaper.com,</li>
      <li>Email: hello@palmgrovepaper.com</li>
      <li>Ph: +1 555 014 2290</li>
    </ul>

    <div class="letter-body">
      <p>Solum nullam principes vis no, eleifend postulant mediocrem ut est, ad tota partem quo. Vix lorem putent<br>no, mea meis solet melius no, pri feugait noluisse appetere no.<br>Ei mea graece suscipit, fastidii probatus est et. Duo ut oportere iudicabit, exerci laoreet vim id. An vidit<br>ceteros phaedrum sit ea. Mollis incorrupte in vix. Noster mnesarchum vix ei.</p>
      <p>Ius te maluisset voluptatum quaerendum, no discere saperet persequeris cum, no pro nonumy partem.<br>Mel mazim corpora te. Has ad aeque mucius impetus,<br>vel tation regione appetere ne. Porro voluptatum ius ut, ei docendi eloquentiam sea. Ne mandamus dolor<br>endi eum, est id tota insolens, eu per facete latine.</p>
      <p>Sea te explicari conceptam definitionem, soluta constituto duo ad, usu an laudem latine voluptaria. Ea<br>repudiare forensibus an.<br>In nam euismod explicari voluptatibus. Petentium dissentiet ex eum, in eam ludus tantas aperiam. Eu<br>feugait suavitate.</p>
      <p>Eum ei augue voluptua copiosae. Vis cu altera noluisse intellegat. At vis probatus perpetua. Tale altera<br>ne quo, est ad</p>
    </div>

    <svg class="foliage foliage--corner" viewBox="0 0 300 275" role="img" aria-label="Cluster of monstera and palm leaves">
      <defs>
        <linearGradient id="cornerLeavesA" x1="0" y1="0" x2="1" y2="1">
          <stop offset="0" stop-color="var(--leaf-mid)"/>
          <stop offset="1" stop-color="var(--leaf-dark)"/>
        </linearGradient>
      </defs>
      <path d="M0 10 C25 0 40 30 45 70 C70 60 95 90 100 115 C130 105 150 130 140 160 C180 175 200 200 195 225 C230 235 265 250 290 275 H0 Z" fill="url(#cornerLeavesA)"/>
    </svg>

    <p class="couple">Lorena<span class="couple__second">&amp; Victor</span></p>
  </section>

  <section class="sheet sheet--blank">
    <svg class="foliage foliage--top" viewBox="0 0 600 190" role="img" aria-label="Border of tropical leaves with pink hibiscus, frangipani flowers and a butterfly">
      <defs>
        <linearGradient id="topLeavesB" x1="0" y1="0" x2="0" y2="1">
          <stop offset="0" stop-color="var(--leaf-mid)"/>
          <stop offset="1" stop-color="var(--leaf-dark)"/>
        </linearGradient>
      </defs>
      <path d="M0 0 H600 V110 C570 130 545 120 520 100 C495 125 470 140 440 120 C410 130 385 125 365 105 C340 135 315 150 285 140 C260 125 235 130 210 118 C190 95 160 92 140 82 C110 100 80 95 55 80 C35 95 15 90 0 85 Z" fill="url(#topLeavesB)"/>
    </svg>

    <svg class="foliage foliage--corner" viewBox="0 0 300 275" role="img" aria-label="Cluster of monstera and palm leaves">
      <defs>
        <linearGradient id="cornerLeavesB" x1="0" y1="0" x2="1" y2="1">
          <stop offset="0" stop-color="var(--leaf-mid)"/>
          <stop offset="1" stop-color="var(--leaf-dark)"/>
        </linearGradient>
      </defs>
      <path d="M0 10 C25 0 40 30 45 70 C70 60 95 90 100 115 C130 105 150 130 140 160 C180 175 200 200 195 225 C230 235 265 250 290 275 H0 Z" fill="url(#cornerLeavesB)"/>
    </svg>

    <p class="couple">Lorena<span class="couple__second">&amp; Victor</span></p>
  </section>

  <h2 class="label label--text">With text letterhead</h2>
  <h2 class="label label--blank">Blank letterhead</h2>

</main>
</body>
</html>
```